Business Card Design

Im a small business that specialises in all aspects of sign installation, big and small, domestic and commercial. I have a construction and carpentry background. I'm after a professional looking business card, that has my logo as the forefront of the card incorporating the same colours as the my logo. No slogan as yet, but open to suggestions. The final design should communicate quality and class workmanship.

Target Market(s)

Managers and Owners of businesses

Industry/Entity Type

Small Business

Contact Information for Business Card

Carwyn Solbeck
Mob: 0417295036
Email: kto.fitouts@quillmail.net

Sign Installation
Property Improvement and Maintenance
Trade Services

Colors
dbdbdb
000000
ffffff

Requirements
Must have
• Logo
My name
My contact details
What I specialise in
Nice to have
• background image/images that are only just noticeable and do not take away from the logo or text.
Should not have
• No colours that contrast from my logo
No heavy machinery images to be used
Logo must stand out

```html
<!DOCTYPE html>
<html lang="en">
<head>
<meta charset="utf-8">
<title>KTO Fitouts – Business Card</title>
<link rel="stylesheet" href="https://fonts.googleapis.com/css2?family=Arimo:wght@400;700&display=swap">
<style>
  :root {
    --backdrop: #dcdfdf;
    --card: #ffffff;
    --brand-blue: #1b3de3;
    --ink: #111111;
    --band-edge: #000000;
  }
  * { margin: 0; padding: 0; box-sizing: border-box; }
  html, body {
    width: 1200px;
    height: 900px;
    overflow: hidden;
    background: var(--backdrop);
    font-family: "Arimo", Arial, sans-serif;
  }
  .canvas {
    position: relative;
    width: 1200px;
    height: 900px;
  }
  .card {
    position: absolute;
    left: 329px;
    width: 522px;
    height: 323px;
    background: var(--card);
    overflow: hidden;
  }
  .card--front { top: 106px; }
  .card--back { top: 477px; }

  .band {
    position: absolute;
    top: 0;
    left: 112px;
    width: 86px;
    height: 100%;
    background: var(--brand-blue);
    border-right: 3px solid var(--band-edge);
  }
  .band-circle {
    position: absolute;
    left: 110px;
    width: 92px;
    height: 92px;
    border-radius: 50%;
    background: var(--card);
  }
  .card--front .band-circle { top: 116px; }
  .card--back .band-circle { top: 114px; }

  .brand-ring {
    position: absolute;
    border-radius: 50%;
    border: 6px solid var(--brand-blue);
  }
  .band-circle .brand-ring {
    left: 5px;
    top: 5px;
    width: 82px;
    height: 82px;
  }

  .company-name {
    position: absolute;
    color: var(--brand-blue);
    font-weight: 700;
    white-space: nowrap;
  }
  .card--front .company-name {
    left: 208px;
    top: 145px;
    font-size: 29px;
    line-height: 34px;
  }

  .brand-lockup {
    position: absolute;
    right: 38px;
    top: 45px;
    display: flex;
    align-items: center;
    gap: 6px;
  }
  .brand-lockup .brand-ring {
    position: static;
    width: 46px;
    height: 46px;
    border-width: 4px;
  }
  .brand-lockup .company-name {
    position: static;
    font-size: 17px;
    line-height: 20px;
  }

  .contact {
    position: absolute;
    right: 38px;
    top: 207px;
    text-align: right;
    color: var(--ink);
  }
  .contact-name {
    font-size: 16px;
    font-weight: 700;
    line-height: 20px;
    margin-bottom: 18px;
  }
  .contact-line {
    font-size: 12.5px;
    line-height: 17px;
  }
</style>
</head>
<body>
  <main class="canvas">
    <section class="card card--front" aria-label="Card front">
      <div class="band"></div>
      <div class="band-circle"><div class="brand-ring"></div></div>
      <div class="company-name">KTO FITOUTS</div>
    </section>

    <section class="card card--back" aria-label="Card back">
      <div class="band"></div>
      <div class="band-circle"><div class="brand-ring"></div></div>
      <div class="brand-lockup">
        <div class="brand-ring"></div>
        <div class="company-name">KTO FITOUTS</div>
      </div>
      <div class="contact">
        <p class="contact-name">Carwyn Solbeck</p>
        <p class="contact-line">Mob: 0417295036</p>
        <p class="contact-line">E-mail: kto.fitouts@quillmail.net</p>
      </div>
    </section>
  </main>
</body>
</html>
```